Custom Branded Sticker for Radon System Alarm

We need a branded sticker for Radon System Alarms. Company colors are #414444 and #01993D, font is Sinkin Sans. This sticker will be used with other stickers for the radon system and will need to match the design. These area also attached. The design is 79.3mm x 79.3mm. There's a 1.5mm blead around the edge. The print area is 76.3mm x 76.3mm. Template is attached with the hole layout area.

Target Market(s)

Homeowners

Industry/Entity Type

Radon Mitigation

Colors

Designer to choose colors to be used in the design.

Requirements
Must have
• Use company colors and match existing system stickers

```html
<!DOCTYPE html>
<html lang="en">
<head>
<meta charset="utf-8">
<title>Mitigation System Alarm Sticker</title>
<link href="https://fonts.googleapis.com/css2?family=Montserrat:wght@300;400;600;700&display=swap" rel="stylesheet">
<style>
  :root {
    --backdrop: #d9dadc;
    --ink: #414444;
    --green: #2b9236;
    --paper: #ffffff;
  }
  html, body {
    margin: 0;
    padding: 0;
    overflow: hidden;
    background: var(--backdrop);
  }
  .canvas {
    width: 1200px;
    height: 1151px;
    background: var(--backdrop);
    overflow: hidden;
  }
  .sticker-sheet {
    display: block;
    width: 1200px;
    height: 1151px;
    font-family: "Montserrat", sans-serif;
  }
  .sticker-body { fill: var(--ink); }
  .stripe { fill: var(--green); }
  .panel-light { fill: var(--paper); }
  .die-cut { fill: var(--backdrop); }
  .brand-box { fill: var(--paper); }
  .brand-name {
    fill: var(--green);
    font-weight: 700;
    font-size: 32px;
    text-anchor: middle;
  }
  .title { font-weight: 600; font-size: 24px; text-anchor: middle; }
  .warning { font-weight: 600; font-size: 25px; text-anchor: middle; letter-spacing: 0.6px; }
  .note { font-weight: 300; font-size: 16.5px; text-anchor: middle; letter-spacing: 0.3px; }
  .action { font-weight: 700; font-size: 16px; text-anchor: middle; }
  .text-dark { fill: var(--ink); }
  .text-light { fill: var(--paper); }
</style>
</head>
<body>
<div class="canvas">
  <svg class="sticker-sheet" viewBox="0 0 1240 1190" preserveAspectRatio="none" xmlns="http://www.w3.org/2000/svg">
    <defs>
      <path id="sticker-outline" d="M550,35 A102,102 0 0 0 688,35 L927,274 L927,318 L688,557 A102,102 0 0 0 550,557 L313,318 L313,274 Z"/>
      <clipPath id="sticker-clip">
        <use href="#sticker-outline"/>
      </clipPath>
      <pattern id="hazard-stripes" width="44" height="44" patternUnits="userSpaceOnUse" patternTransform="rotate(-45)">
        <rect class="stripe" x="0" y="0" width="25" height="44"/>
      </pattern>
      <g id="die-cuts">
        <circle class="die-cut" cx="683" cy="142" r="46"/>
        <circle class="die-cut" cx="740" cy="236" r="16"/>
        <circle class="die-cut" cx="760" cy="436" r="12"/>
        <rect class="die-cut" x="290" y="272" width="72" height="48" rx="24"/>
        <rect class="die-cut" x="878" y="272" width="72" height="48" rx="24"/>
      </g>
    </defs>

    <!-- Light panel variant -->
    <g class="sticker sticker--light-panel">
      <g clip-path="url(#sticker-clip)">
        <use class="sticker-body" href="#sticker-outline"/>
        <rect x="313" y="35" width="614" height="100" fill="url(#hazard-stripes)"/>
        <rect x="313" y="217" width="614" height="38" fill="url(#hazard-stripes)"/>
        <path class="panel-light" d="M338,256 L902,256 L902,318 L692,528 A102,102 0 0 0 548,528 L338,318 Z"/>
        <use href="#die-cuts"/>
      </g>
      <text class="brand-name" x="541" y="190" textLength="164" lengthAdjust="spacingAndGlyphs">CLEARAIR</text>
      <text class="title text-dark" x="620" y="293">Mitigation System Alarm</text>
      <text class="warning text-dark" x="620" y="323">DO NOT ALTER OR DISCONNECT</text>
      <text class="note text-dark" x="620" y="358">Alarm/Red LED = System Malfunction</text>
      <text class="note text-dark" x="620" y="378">Alarm will automatically reset when</text>
      <text class="note text-dark" x="620" y="398">vacuum pressure is restored.</text>
      <text class="note text-dark" x="620" y="418">Alarm will chirp when battery is low</text>
      <text class="action text-dark" x="622" y="462">Press test/reset button</text>
      <text class="action text-dark" x="622" y="482">to silence alarm.</text>
    </g>

    <!-- Dark panel variant -->
    <g class="sticker sticker--dark-panel" transform="translate(0,594)">
      <g clip-path="url(#sticker-clip)">
        <use class="sticker-body" href="#sticker-outline"/>
        <rect x="313" y="35" width="614" height="100" fill="url(#hazard-stripes)"/>
        <rect x="313" y="217" width="614" height="38" fill="url(#hazard-stripes)"/>
        <use href="#die-cuts"/>
      </g>
      <rect class="brand-box" x="453" y="146" width="176" height="62"/>
      <text class="brand-name" x="541" y="189" textLength="150" lengthAdjust="spacingAndGlyphs">CLEARAIR</text>
      <text class="title text-light" x="620" y="293">Mitigation System Alarm</text>
      <text class="warning text-light" x="620" y="323">DO NOT ALTER OR DISCONNECT</text>
      <text class="note text-light" x="620" y="358">Alarm/Red LED = System Malfunction</text>
      <text class="note text-light" x="620" y="378">Alarm will automatically reset when</text>
      <text class="note text-light" x="620" y="398">vacuum pressure is restored.</text>
      <text class="note text-light" x="620" y="418">Alarm will chirp when battery is low</text>
      <text class="action text-light" x="622" y="462">Press test/reset button</text>
      <text class="action text-light" x="622" y="482">to silence alarm.</text>
    </g>
  </svg>
</div>
</body>
</html>
```